K9 Orbit needs a business card designed

We need a business card designed for K9 Orbit, an expansion of K9 Technics Pty Ltd (www.k9technics.com.au)

We provide high quality professional services for the Australian space industry. Our clients include the Southern Stellar Bureau and companies working in the space industry. We identify people with space related skills both locally and internationally who are then contracted by clients to create products and support space launch activities.

Colours to be used:
- Navy blue #000080
- Rocket metallic #8A7F8D
- Platinum #E5E4E2
- Black #000000
- White #FFFFFF

*Front of the card*
I have attached our K9 Orbit logo, which needs to be the main item on the card. The 'Space' text should be placed to the right of the 'K9' part rather than below, similar to the attached K9 Technics card, which this card should match.

If subtext is included, however, it should read ‘Labour Hire • Consultancy • Project Delivery’ rather than the ‘Design • Build • Test • Maintain’ of the K9 Technics card.

A black background (rather than blue background in the K9 Technics card) might be good, with a white pattern as in the K9 Technics card. If colour is used, the logo should be in its standard colours (as provided for the K9 Orbit logo).

*Back of the card*
Include a smaller K9 Orbit logo on the back.

We need the following details for K9 Orbit personnel (as a template for entry):
- Name
- Company Position
- Mobile Number
- Email
- Office Address
- Include the K9 Orbit website: www.k9orbit.com.au

Overall, we'd like to see a design that communicates the adventure of space, professional integrity, and customer service. We look forward to seeing what you can come up with.

Target Market(s)

We provide high quality professional services for the Australian space industry. Our clients include the Southern Stellar Bureau and companies working in the space industry.

Contact Information for Business Card

- Name
- Company Position
- Mobile Number
- Email
- Office Address

Requirements
Must have
• See project description.

```html
<!DOCTYPE html>
<html lang="en">
<head>
<meta charset="utf-8">
<title>K9 Orbit Business Card</title>
<link href="https://fonts.googleapis.com/css2?family=Montserrat:wght@400;500;700&display=swap" rel="stylesheet">
<style>
  :root {
    --backdrop: #1c1c1f;
    --navy: #25246f;
    --navy-soft: #2c2c7c;
    --metal: #8a7f8d;
    --white: #ffffff;
    --ink-grey: #9a96a0;
  }
  * { box-sizing: border-box; margin: 0; padding: 0; }
  html, body { width: 1200px; height: 909px; overflow: hidden; }
  body {
    background: var(--backdrop);
    font-family: "Montserrat", sans-serif;
    position: relative;
  }
  .card {
    position: absolute;
    left: 330px;
    width: 540px;
    height: 310px;
    overflow: hidden;
    box-shadow: 0 10px 30px rgba(0,0,0,.5);
  }
  /* Front */
  .card-front { top: 90px; background: var(--navy); color: var(--white); }
  .front-halo {
    position: absolute; left: 150px; top: 20px;
    width: 270px; height: 270px; border-radius: 50%;
    background: var(--navy-soft); opacity: .55;
  }
  .front-brand {
    position: absolute; left: 0; right: 0; top: 112px;
    text-align: center;
    font-weight: 500; font-size: 40px; letter-spacing: 12px;
  }
  .front-tagline {
    position: absolute; left: 0; right: 0; top: 196px;
    text-align: center; font-size: 11.5px; font-weight: 500; letter-spacing: .6px;
  }
  /* Back */
  .card-back { top: 500px; background: var(--white); }
  .back-brand {
    position: absolute; left: 205px; top: 50px;
    display: flex; align-items: center; gap: 12px;
    color: var(--navy); font-weight: 700; font-size: 30px; letter-spacing: 8px;
  }
  .brand-dot { width: 16px; height: 16px; border-radius: 50%; background: var(--navy); }
  .back-tagline {
    position: absolute; left: 234px; top: 98px;
    color: var(--navy); font-size: 7px; font-weight: 500; letter-spacing: .3px;
  }
  .person { position: absolute; left: 40px; top: 138px; text-align: right; width: 170px; }
  .person-name { color: var(--navy); font-weight: 700; font-size: 20px; }
  .person-role { color: var(--ink-grey); font-size: 16px; margin-top: 2px; }
  .divider { position: absolute; left: 226px; top: 138px; width: 1px; height: 62px; background: var(--metal); }
  .contacts { position: absolute; left: 240px; top: 136px; list-style: none; }
  .contacts li {
    display: flex; align-items: center; gap: 8px;
    color: var(--ink-grey); font-size: 13px; line-height: 21px;
  }
  .contacts svg { width: 11px; height: 11px; fill: var(--navy); flex: none; }
  .address-band {
    position: absolute; left: 0; right: 0; bottom: 26px; height: 30px;
    background: var(--navy); color: var(--white);
    display: flex; align-items: center; padding-left: 40px;
    font-size: 13px; font-weight: 500;
  }
</style>
</head>
<body>
  <section class="card card-front" aria-label="Card front">
    <div class="front-halo"></div>
    <div class="front-brand">K9 ORBIT</div>
    <p class="front-tagline">Consultancy • Command • Control • Communications • Labour Hire</p>
  </section>

  <section class="card card-back" aria-label="Card back">
    <div class="back-brand"><span class="brand-dot"></span>K9 ORBIT</div>
    <p class="back-tagline">Consultancy • Control • Communications • Labour Hire</p>

    <div class="person">
      <p class="person-name">Jordan Pellow</p>
      <p class="person-role">President</p>
    </div>
    <div class="divider"></div>
    <ul class="contacts">
      <li><svg viewBox="0 0 24 24"><path d="M6.6 10.8a15 15 0 0 0 6.6 6.6l2.2-2.2a1 1 0 0 1 1-.25 11.4 11.4 0 0 0 3.6.57 1 1 0 0 1 1 1V20a1 1 0 0 1-1 1A17 17 0 0 1 3 4a1 1 0 0 1 1-1h3.5a1 1 0 0 1 1 1c0 1.25.2 2.45.57 3.57a1 1 0 0 1-.25 1z"/></svg>555.204.1187</li>
      <li><svg viewBox="0 0 24 24"><path d="M2 5h20v14H2z M2 5l10 8 10-8" /></svg>northwindcrew@mail.com</li>
      <li><svg viewBox="0 0 24 24"><circle cx="12" cy="12" r="10"/></svg>www.northwindcrew.com</li>
    </ul>

    <div class="address-band">18 Harbor Lane Brookfield, WA 6021</div>
  </section>
</body>
</html>
```